Visitenkarten und Briefpapier für Beratungsunternehmen
Zielgruppe
Führungskräfte im Gesundheits- und Sozialwesen-
Aufgabenstellung
Wir suchen ein Set aus Briefpapier und Visitenkarten zu umserem Logo. Beides darf (muss nicht) beidseitig gestaltet werden.

```html
<!DOCTYPE html>
<html lang="de">
<head>
<meta charset="utf-8">
<title>Kelmarante – Visitenkarten</title>
<link href="https://fonts.googleapis.com/css2?family=Open+Sans:wght@400;600;700&display=swap" rel="stylesheet">
<style>
  :root {
    --board-top: #ffffff;
    --board-bottom: #c4c5c8;
    --label-top: #a9a9ab;
    --label-bottom: #ffffff;
    --blue-light: #0b8fd6;
    --blue-dark: #0a3a8f;
    --navy: #17368a;
    --green: #3aaa35;
    --paper: #ffffff;
    --ink-white: #ffffff;
  }
  * { margin: 0; padding: 0; box-sizing: border-box; }
  html, body { width: 1200px; height: 1200px; overflow: hidden; }
  body {
    font-family: "Open Sans", Arial, sans-serif;
    background: linear-gradient(180deg, var(--board-top) 0%, #f1f1f2 30%, var(--board-bottom) 100%);
    position: relative;
  }
  .label {
    position: absolute;
    width: 485px;
    text-align: center;
    font-size: 19px;
    letter-spacing: 0.2px;
  }
  .label--top { color: var(--label-top); top: 116px; }
  .label--bottom { color: var(--label-bottom); top: 562px; }
  .col-1 { left: 88px; }
  .col-2 { left: 625px; }

  .card {
    position: absolute;
    width: 485px;
    height: 313px;
    box-shadow: 2px 4px 8px rgba(0,0,0,0.28);
  }
  .row-1 { top: 155px; }
  .row-2 { top: 600px; }
  .card--blue { background: linear-gradient(180deg, var(--blue-light) 0%, #0b62b6 50%, var(--blue-dark) 100%); }
  .card--white { background: var(--paper); border: 1px solid #cfd3de; }

  .brand {
    position: absolute;
    text-align: center;
  }
  .brand__dot {
    display: block;
    margin: 0 auto;
    border-radius: 50%;
    background: var(--green);
  }
  .brand__name {
    display: block;
    font-weight: 700;
    line-height: 1;
    letter-spacing: -0.5px;
  }
  .brand__tagline {
    display: block;
    color: var(--green);
    font-weight: 700;
  }
  .card--blue .brand__name { color: var(--ink-white); }
  .card--white .brand__name { color: var(--navy); }

  .brand--back { left: 0; right: 0; top: 70px; }
  .brand--back .brand__dot { width: 50px; height: 50px; margin-bottom: 30px; }
  .brand--back .brand__name { font-size: 41px; }
  .brand--back .brand__tagline { font-size: 13px; margin-top: 2px; }

  .brand--front { left: 250px; width: 215px; top: 20px; }
  .brand--front .brand__dot { width: 36px; height: 36px; margin-bottom: 20px; }
  .brand--front .brand__name { font-size: 31px; }
  .brand--front .brand__tagline { font-size: 10.5px; margin-top: 1px; }

  .person {
    position: absolute;
    left: 28px;
    top: 153px;
  }
  .person__name { color: var(--green); font-weight: 700; font-size: 14px; line-height: 1.2; }
  .person__role { font-size: 11px; line-height: 1.3; }
  .card--blue .person__role { color: var(--ink-white); }
  .card--white .person__role { color: var(--navy); }

  .contact {
    position: absolute;
    left: 255px;
    top: 175px;
    font-size: 11px;
    line-height: 14px;
  }
  .card--blue .contact { color: var(--ink-white); }
  .card--white .contact { color: var(--navy); }
  .contact__company { font-weight: 700; margin-bottom: 5px; }
  .contact__group { margin-bottom: 6px; }
  .contact__web { color: var(--green); font-weight: 700; }
</style>
</head>
<body>
  <div class="label label--top col-1">Rückseite 1</div>
  <div class="label label--top col-2">Rückseite 2</div>
  <div class="label label--bottom col-1">Frontseite 1</div>
  <div class="label label--bottom col-2">Frontseite 2</div>

  <section class="card card--blue row-1 col-1">
    <div class="brand brand--back">
      <span class="brand__dot"></span>
      <span class="brand__name">KELMARANTE</span>
      <span class="brand__tagline">Klarheit durch Erfahrung</span>
    </div>
  </section>

  <section class="card card--white row-1 col-2">
    <div class="brand brand--back">
      <span class="brand__dot"></span>
      <span class="brand__name">KELMARANTE</span>
      <span class="brand__tagline">Klarheit durch Erfahrung</span>
    </div>
  </section>

  <section class="card card--blue row-2 col-1">
    <div class="brand brand--front">
      <span class="brand__dot"></span>
      <span class="brand__name">KELMARANTE</span>
      <span class="brand__tagline">Klarheit durch Erfahrung</span>
    </div>
    <div class="person">
      <div class="person__name">Lena Hartwig</div>
      <div class="person__role">Geschäftsführerin</div>
    </div>
    <div class="contact">
      <div class="contact__company">Kelmarante UG (Haftungsbeschränkt)</div>
      <div class="contact__group">Lindenweg 14<br>50321 Brühlingen</div>
      <div class="contact__group">Fon&nbsp; +49 (0) 23456781-4<br>Fax&nbsp; +49 (0) 23456781-15</div>
      <div>info@kelmarante.de</div>
      <div class="contact__web">www.kelmarante.de</div>
    </div>
  </section>

  <section class="card card--white row-2 col-2">
    <div class="brand brand--front">
      <span class="brand__dot"></span>
      <span class="brand__name">KELMARANTE</span>
      <span class="brand__tagline">Klarheit durch Erfahrung</span>
    </div>
    <div class="person">
      <div class="person__name">Lena Hartwig</div>
      <div class="person__role">Geschäftsführerin</div>
    </div>
    <div class="contact">
      <div class="contact__company">Kelmarante UG (Haftungsbeschränkt)</div>
      <div class="contact__group">Lindenweg 14<br>50321 Brühlingen</div>
      <div class="contact__group">Fon&nbsp; +49 (0) 23456781-4<br>Fax&nbsp; +49 (0) 23456781-15</div>
      <div>info@kelmarante.de</div>
      <div class="contact__web">www.kelmarante.de</div>
    </div>
  </section>
</body>
</html>
```